Web design for our new company

We need a web design for our product and for our company.
And the main is our Product tool called "velmora".
----------------------------------------------------------
[Our company's Goal]
Make organization’s communication smooth and healthy with transparency and efficiency for works and tasks in all levels with our workflow tool.

[Our Mission]
Our mission is to achieve business goals with customers.
We work together to identify the goals for your company, guides your strategy and bring the technology answers which best fit to achieve the goals.

[What we do]
We have a workflow tool "velmora"
- Very simple end-user configurable workflow for any company processes
(Targeting small-med size company)
- Graphical & fun features for startup users
- Simple and easy task control with quillbox e-mail look & feel
- Non charged skill up guidance
- Additional features with;
Multiple delegation
Clear status for each owner
Task owner management console with due date reminders&reporting

Others
1. System Development & Implementation Service
Our client list includes a wide variety of small to medium to major sized enterprises.
We can offer from full-scratch based development to packaged system implementation.

2. Project Management(PM) Service
We will provide end-to-end PM service with experienced PM.
Our service is not only “managing” but “leading” to bring success to achieve the goal.

3.Consultation Service

Consulting services to a wide range of fields such as creating business strategy, business process Kaizen, IT system consultation and change management.

Target Market(s)

Business to Business
Mainly to medium size - startup company

Industry/Entity Type

It Company

Coding

Coded - Design and coding required

Number of Pages Required

5+ page

Colors
0255a3
33a6d7
86cfc6
33b8a4
add136
cadf82
fbf289
fee18a
faa54b

Requirements
Must have
• We need Pages for
• Company mission
• Service Overview
• Contact
• Privacy Policy
• Terms and Conditions
• =========================
• As there were some questions, I add followings.---------
• 1. File Format
• We are going to use Brixel cloud services to upload finished web files.
• The finished files should be ready to use by simply replacing images and text.
• Please provide me "easy to handle" template with "sophisticated design".
• Thanks!
• 2. Multiple Languages
• We need buttons for changing language.
• We will have this translated to German, English and Japanese.
• Thank you so much!!
Nice to have
• These are current Logos and will be a next project to revise them...
• Attached Company Profile and Logo design
• 1. Company Profile
• 2. Our Company Logo
• 3. Our Product Logo -> This is most close to our image of design base.
• 4. Product Logo for PPT Header
• All just for your reference.
• ---------
• As there were some request, I added attachment as for contents for Our mission page.
Should not have
• I hope to see some unique designs.
• (Sorry please ignore my last update as I checked with our CEO.
• Bootstrap is absolutely good template.)

```html
<!DOCTYPE html>
<html lang="en">
<head>
<meta charset="utf-8">
<title>Telvaro e.U. – Workflow Tool</title>
<link href="https://fonts.googleapis.com/css2?family=Roboto+Condensed:wght@400;700&display=swap" rel="stylesheet">
<style>
  :root {
    --lime: #add136;
    --lime-dark: #8fb12a;
    --olive: #5e7a1e;
    --olive-deep: #4a621a;
    --ink: #222;
    --muted: #555;
    --white: #fff;
    --blue: #33a6d7;
    --navy: #0255a3;
    --box: rgba(230, 228, 205, 0.82);
  }
  * { box-sizing: border-box; margin: 0; padding: 0; }
  html, body { width: 1200px; height: 800px; overflow: hidden; }
  body { font-family: "Roboto Condensed", Arial, sans-serif; color: var(--ink); background: var(--white); }
  .page { width: 1200px; height: 800px; display: flex; flex-direction: column; }
  .page > * { flex-shrink: 0; overflow: hidden; }

  .topbar { height: 16px; background: var(--lime); display: flex; justify-content: flex-end; align-items: center; gap: 22px; padding-right: 90px; font-size: 9px; color: var(--ink); }
  .topbar span { display: flex; align-items: center; gap: 5px; }

  .nav { height: 32px; display: flex; align-items: center; justify-content: space-between; padding: 0 120px 0 90px; border-bottom: 1px solid #eee; }
  .brand { display: flex; align-items: center; gap: 6px; font-size: 18px; font-weight: 700; color: var(--ink); }
  .brand-dot { width: 12px; height: 12px; border-radius: 50%; border: 2px solid var(--lime-dark); }
  .menu { display: flex; gap: 12px; font-size: 9px; text-transform: uppercase; }
  .menu a { color: var(--ink); text-decoration: none; padding: 1px 5px; }
  .menu a.active { background: var(--lime); }

  .hero { height: 192px; position: relative; }
  .hero-photo { position: absolute; inset: 0; background: linear-gradient(100deg, #7d8a5c 0%, #5a6448 35%, #2c3747 60%, #47503c 85%, #8e9a6e 100%); }
  .hero-tint { position: absolute; inset: 0; background: rgba(120, 140, 40, 0.25); }
  .hero-copy { position: absolute; left: 150px; top: 54px; color: var(--white); max-width: 720px; }
  .hero-copy h1 { font-size: 24px; font-weight: 400; line-height: 1.15; }
  .btn { display: inline-block; background: var(--lime); color: var(--ink); font-size: 9px; padding: 3px 14px; text-decoration: none; }
  .hero .btn { margin-top: 10px; }

  .mission { height: 140px; display: flex; justify-content: space-between; align-items: center; padding: 0 150px; }
  .mission-text { width: 440px; }
  .mission h2 { font-size: 14px; margin-bottom: 6px; }
  .mission p { font-size: 10px; line-height: 1.5; color: var(--muted); margin-bottom: 8px; }
  .mission-photo { width: 300px; height: 104px; background: linear-gradient(135deg, #6b4a36, #b99a7e 45%, #3d3f44 80%); box-shadow: 0 1px 3px rgba(0,0,0,.3); }

  .services { height: 150px; position: relative; }
  .services-photo { position: absolute; inset: 0; background: linear-gradient(120deg, var(--olive) 0%, #6d8a25 50%, var(--olive-deep) 100%); }
  .services-inner { position: relative; padding-top: 8px; color: var(--white); text-align: center; }
  .services h2 { font-size: 12px; font-weight: 400; text-decoration: underline; margin-bottom: 4px; }
  .service-row { display: flex; justify-content: center; gap: 50px; }
  .service { width: 300px; display: flex; flex-direction: column; align-items: center; }
  .service-head { display: flex; align-items: center; gap: 8px; height: 30px; font-size: 12px; line-height: 1.15; text-align: left; align-self: flex-start; }
  .service-icon { width: 28px; height: 28px; border-radius: 50%; background: var(--white); display: flex; align-items: center; justify-content: center; flex-shrink: 0; }
  .service-box { width: 250px; height: 56px; background: var(--box); color: #333; font-size: 8.5px; line-height: 1.4; text-align: left; padding: 7px 10px; margin: 6px 0 7px; }
  .service .btn { background: var(--white); font-size: 8px; padding: 2px 18px; }

  .tool { height: 182px; display: flex; align-items: center; padding: 0 150px 0 170px; gap: 60px; }
  .tool-mark { display: flex; align-items: center; gap: 8px; font-size: 22px; font-weight: 700; color: var(--ink); width: 140px; flex-shrink: 0; }
  .tool-mark-dot { width: 12px; height: 12px; border-radius: 50%; background: var(--lime); flex-shrink: 0; }
  .tool-body { flex: 1; }
  .tool h2 { font-size: 11px; font-weight: 400; color: var(--blue); text-decoration: underline; margin-bottom: 12px; margin-left: 120px; }
  .tool ul { list-style: none; font-size: 11px; line-height: 15px; }
  .tool li { display: flex; align-items: center; gap: 6px; }
  .tool li.sub { padding-left: 14px; }
  .tool li.sub::before { content: "•"; }

  .footer { height: 88px; background: var(--lime); display: flex; justify-content: space-between; padding: 16px 150px 0; font-size: 8px; color: #233; }
  .footer h3 { font-size: 9px; font-weight: 400; text-decoration: underline; margin-bottom: 4px; }
  .footer p { line-height: 1.4; }
  .foot-about { width: 220px; }
  .social { display: flex; gap: 4px; }
  .social i { width: 9px; height: 9px; border-radius: 50%; background: #1c2b14; display: block; }
</style>
</head>
<body>
<div class="page">
  <div class="topbar">
    <span><svg width="8" height="8" viewBox="0 0 24 24"><path fill="#222" d="M6.6 10.8a15 15 0 006.6 6.6l2.2-2.2c.3-.3.7-.4 1-.2 1.1.4 2.3.6 3.6.6.6 0 1 .4 1 1V20c0 .6-.4 1-1 1A17 17 0 013 4c0-.6.4-1 1-1h3.5c.6 0 1 .4 1 1 0 1.3.2 2.5.6 3.6.1.3 0 .7-.2 1z"/></svg>+43 1 234 5678</span>
    <span><svg width="8" height="8" viewBox="0 0 24 24"><path fill="#222" d="M12 2a7 7 0 00-7 7c0 5 7 13 7 13s7-8 7-13a7 7 0 00-7-7zm0 9.5a2.5 2.5 0 110-5 2.5 2.5 0 010 5z"/></svg>Lindenweg 12, 1010 Wien</span>
  </div>

  <header class="nav">
    <div class="brand"><span class="brand-dot"></span>Telvaro e.U.</div>
    <nav class="menu">
      <a class="active" href="#">Home</a><a href="#">About us</a><a href="#">Products</a><a href="#">Pricing &amp; Policy</a><a href="#">Contact</a>
    </nav>
  </header>

  <section class="hero">
    <div class="hero-photo" role="img" aria-label="Photo of a businessman in a dark suit gesturing with an open hand"></div>
    <div class="hero-tint"></div>
    <div class="hero-copy">
      <h1>Make organization's communication smooth and healthy<br>with transparency and efficiency for works and tasks<br>in all levels with our workflow tool.</h1>
      <a class="btn" href="#">Get Started</a>
    </div>
  </section>

  <section class="mission">
    <div class="mission-text">
      <h2>Our Mission</h2>
      <p>Our mission is to achieve business goals with customers.<br>We work together to identify the goals for your company, guides your strategy and bring the technology answers which best fit to achieve the goals. We listen first, plan together and deliver step by step so every team can see progress clearly.</p>
      <a class="btn" href="#">Know more</a>
    </div>
    <div class="mission-photo" role="img" aria-label="Photo of a team joining hands over a desk with laptops"></div>
  </section>

  <section class="services">
    <div class="services-photo" role="img" aria-label="Green-tinted photo of a desk with laptop and documents"></div>
    <div class="services-inner">
      <h2>What we do</h2>
      <div class="service-row">
        <div class="service">
          <div class="service-head"><span class="service-icon"><svg width="15" height="15" viewBox="0 0 24 24" fill="none" stroke="#333" stroke-width="2"><rect x="4" y="4" width="16" height="16" rx="2"/><path d="M8 12l3 3 5-6"/></svg></span>Project Management(PM) Service</div>
          <div class="service-box">We will provide end-to-end PM service with experienced PM. Our service is not only "managing" but "leading" to bring success to achieve the goal.</div>
          <a class="btn" href="#">Know more</a>
        </div>
        <div class="service">
          <div class="service-head"><span class="service-icon"><svg width="15" height="15" viewBox="0 0 24 24" fill="none" stroke="#333" stroke-width="2"><rect x="3" y="4" width="18" height="12" rx="1"/><path d="M8 20h8M12 16v4"/></svg></span>System Development &amp;<br>Implementation Service</div>
          <div class="service-box">Our client list includes a wide variety of small to medium to major sized enterprises. We can offer from full-scratch based development to packaged system implementation.</div>
          <a class="btn" href="#">Know more</a>
        </div>
        <div class="service">
          <div class="service-head"><span class="service-icon"><svg width="15" height="15" viewBox="0 0 24 24" fill="none" stroke="#333" stroke-width="2"><circle cx="12" cy="12" r="8"/><path d="M12 7v5l3 3"/></svg></span>Consultation Service</div>
          <div class="service-box">Consulting services to a wide range of fields such as creating business strategy, business process Kaizen, IT system consultation and change management.</div>
          <a class="btn" href="#">Know more</a>
        </div>
      </div>
    </div>
  </section>

  <section class="tool">
    <div class="tool-mark"><span class="tool-mark-dot"></span>velmora</div>
    <div class="tool-body">
      <h2>A Brief about our workflow tool</h2>
      <ul>
        <li><svg width="10" height="10" viewBox="0 0 24 24" fill="none" stroke="#0255a3" stroke-width="2.5"><rect x="3" y="3" width="18" height="18"/><path d="M7 12l4 4 7-9"/></svg>Very simple end-user configurable workflow for any company processes.</li>
        <li><svg width="10" height="10" viewBox="0 0 24 24" fill="none" stroke="#0255a3" stroke-width="2.5"><rect x="3" y="3" width="18" height="18"/><path d="M7 12l4 4 7-9"/></svg>Graphical and fun features for startup users.</li>
        <li><svg width="10" height="10" viewBox="0 0 24 24" fill="none" stroke="#0255a3" stroke-width="2.5"><rect x="3" y="3" width="18" height="18"/><path d="M7 12l4 4 7-9"/></svg>Simple and easy task control with quillbox e-mail look and feel.</li>
        <li><svg width="10" height="10" viewBox="0 0 24 24" fill="none" stroke="#0255a3" stroke-width="2.5"><rect x="3" y="3" width="18" height="18"/><path d="M7 12l4 4 7-9"/></svg>Non charged skill up guidance.</li>
        <li><svg width="10" height="10" viewBox="0 0 24 24" fill="none" stroke="#0255a3" stroke-width="2.5"><rect x="3" y="3" width="18" height="18"/><path d="M7 12l4 4 7-9"/></svg>Additional features with:</li>
        <li class="sub">Multiple delegation.</li>
        <li class="sub">Clear status for each owner.</li>
        <li class="sub">Task owner management console with due date reminders and reporting.</li>
      </ul>
    </div>
  </section>

  <footer class="footer">
    <div class="foot-about">
      <h3>About us</h3>
      <p>Make organization's communication smooth and healthy with transparency and efficiency for works and tasks in all levels with our workflow tool.</p>
    </div>
    <div>
      <h3>Company</h3>
      <p>About us<br>Products<br>Pricing &amp; Policy<br>Contact us</p>
    </div>
    <div>
      <h3>Contact Info</h3>
      <p>+43 1 234 5678<br>Lindenweg 12, 1010 Wien<br>info@telvaro.example</p>
    </div>
    <div>
      <h3>Follow Us</h3>
      <div class="social"><i></i><i></i><i></i><i></i></div>
    </div>
  </footer>
</div>
</body>
</html>
```